Clearpath Ledger Billing Company Business card

Need a business card that stands out that includes name of company,(above) Owners name Marisol Whitfield phone#555-314-7762 email# ClearpathLedgerBC@mailbox-example.com and website www.Clearpathledgerbillingcompany-example.com. This is a medical billing company so the card has to relate to that or relate to steady cashflow

```html
<!DOCTYPE html>
<html lang="en">
<head>
<meta charset="utf-8">
<title>Clearpath Ledger Billing Company – Business Card</title>
<link href="https://fonts.googleapis.com/css2?family=Libre+Franklin:wght@400;600&display=swap" rel="stylesheet">
<style>
  :root {
    --navy: #0b4488;
    --green: #7ab929;
    --white: #ffffff;
    --paper-light: #ffffff;
    --paper-shade: #e3e4e6;
    --ink-grey: #5a5c60;
    --stage: #ecebe8;
  }
  * { box-sizing: border-box; margin: 0; padding: 0; }
  html, body {
    width: 1200px; height: 950px; overflow: hidden;
    background: var(--stage);
    font-family: "Libre Franklin", Arial, sans-serif;
  }
  .canvas {
    width: 1200px; height: 950px;
    display: flex; flex-direction: column; align-items: center; justify-content: center;
    gap: 44px;
  }
  .card {
    width: 720px; height: 411px;
    position: relative; overflow: hidden;
    box-shadow: 0 6px 18px rgba(0,0,0,.18);
    background: linear-gradient(135deg, var(--paper-light) 30%, var(--paper-shade) 100%);
  }

  /* Front */
  .card-front { display: flex; }
  .contact-panel {
    width: 410px; height: 100%;
    background: var(--navy);
    border-right: 3px solid var(--green);
    color: var(--white);
    padding: 74px 0 0 42px;
  }
  .owner-name { font-size: 25px; font-weight: 600; letter-spacing: .2px; }
  .owner-title { font-size: 15px; font-weight: 400; margin-top: 4px; }
  .contact-list { list-style: none; margin-top: 30px; font-size: 14.5px; line-height: 1.6; }
  .contact-list b { font-weight: 600; margin-right: 4px; }
  .brand-panel {
    flex: 1;
    display: flex; align-items: center; justify-content: center;
    padding: 0 24px;
  }

  /* Brand name block */
  .brand {
    display: flex; align-items: center; gap: 12px;
    color: var(--navy); font-weight: 600; text-transform: uppercase;
    letter-spacing: 1px; line-height: 1.25; text-align: left;
  }
  .brand-mark { width: 14px; height: 14px; background: var(--green); flex: none; }
  .brand-front { font-size: 17px; }
  .brand-back { font-size: 26px; }

  /* Back */
  .card-back {
    display: flex; flex-direction: column; align-items: center; justify-content: center;
    gap: 30px;
  }
  .back-web { font-size: 16px; color: var(--ink-grey); letter-spacing: .3px; }
</style>
</head>
<body>
<main class="canvas">
  <section class="card card-front" aria-label="Business card front">
    <div class="contact-panel">
      <h1 class="owner-name">Marisol Whitfield</h1>
      <p class="owner-title">Owners</p>
      <ul class="contact-list">
        <li><b>P:</b>555-314-7762</li>
        <li><b>E:</b>ClearpathLedgerBC@mailbox-example.com</li>
        <li><b>W:</b>Clearpathledgerbillingcompany-example.com</li>
      </ul>
    </div>
    <div class="brand-panel">
      <div class="brand brand-front">
        <span class="brand-mark" aria-hidden="true"></span>
        <span>Clearpath Ledger<br>Billing Company</span>
      </div>
    </div>
  </section>

  <section class="card card-back" aria-label="Business card back">
    <div class="brand brand-back">
      <span class="brand-mark" aria-hidden="true"></span>
      <span>Clearpath Ledger<br>Billing Company</span>
    </div>
    <p class="back-web">www.Clearpathledgerbillingcompany-example.com</p>
  </section>
</main>
</body>
</html>
```